KOVA WIRING PTE LTD
KOVA WIRING NAME CARD
Project: KOVA WIRING PTE LTD
KOVA WIRING PTE LTD - Engineering
Creative Brief
Professional
Deren Whitcombe
Manager
57 Tannery Lane #03-22 Silverbrook Industrial Complex Singapore 347912
derenkovawiring@mailbox-example.net
Reg No. 198733502K
https://www.filevault-example.net/share/7qe2kx9/ZTRmPwq4HnLc?dl=0 Pleas find folder for the logo design A.I. file. Thanks Client love the 3 colour in the logo design for FengShui purposes.
harlowbek harlowbek
Hi my client like your design #218, Can you give the stationary set for #218. We try to finalize by tomorrow. Thanks

```html
<!DOCTYPE html>
<html lang="en">
<head>
<meta charset="utf-8">
<title>Kova Wiring Name Card</title>
<link href="https://fonts.googleapis.com/css2?family=Lato:wght@400;700&display=swap" rel="stylesheet">
<style>
  :root {
    --bg: #e9e7e3;
    --card-white: #ffffff;
    --card-black: #0b0b0b;
    --green: #1f8a3d;
    --blue: #2b3f9e;
    --navy: #1b1f4a;
    --ink: #2c2c2c;
    --muted: #6a6a6a;
  }
  * { box-sizing: border-box; margin: 0; padding: 0; }
  html, body { width: 1200px; height: 904px; overflow: hidden; }
  body {
    background: var(--bg);
    font-family: "Lato", Arial, sans-serif;
    color: var(--ink);
    position: relative;
  }
  .card {
    position: absolute;
    left: 250px;
    width: 700px;
    height: 400px;
    border-radius: 4px;
    box-shadow: 0 6px 18px rgba(0,0,0,0.18);
    overflow: hidden;
  }
  .card-back { top: 36px; background: var(--card-black); }
  .card-front { top: 468px; background: var(--card-white); }

  .back-mark {
    position: absolute;
    left: 50%; top: 50%;
    transform: translate(-50%, -50%);
    display: flex; align-items: center; gap: 14px;
  }
  .mark-square {
    width: 46px; height: 46px;
    background: var(--green);
  }
  .back-mark .brand-name {
    color: #ffffff;
    font-size: 26px;
    font-weight: 700;
    letter-spacing: 2px;
  }

  .front-brand {
    position: absolute;
    left: 42px; top: 56px;
    display: flex; align-items: center; gap: 12px;
  }
  .front-brand .mark-square { width: 40px; height: 40px; }
  .front-brand .brand-name {
    color: var(--navy);
    font-size: 28px;
    font-weight: 700;
    letter-spacing: 2px;
  }

  .person {
    position: absolute;
    right: 90px; top: 138px;
    text-align: center;
  }
  .person-name { color: var(--green); font-size: 17px; font-weight: 700; }
  .person-role { color: var(--muted); font-size: 12px; margin-top: 3px; }

  .address {
    position: absolute;
    left: 42px; top: 150px;
    font-size: 12.5px; line-height: 17px;
    color: var(--ink);
  }

  .contacts {
    position: absolute;
    left: 42px; top: 222px;
    list-style: none;
    font-size: 12.5px; line-height: 17px;
  }
  .contacts li { display: flex; align-items: center; gap: 8px; }
  .contacts svg { width: 11px; height: 11px; flex: none; }

  .bands { position: absolute; left: 0; bottom: 0; width: 700px; height: 140px; }
</style>
</head>
<body>

<section class="card card-back" aria-label="Card back">
  <div class="back-mark">
    <span class="mark-square"></span>
    <span class="brand-name">KOVA WIRING</span>
  </div>
</section>

<section class="card card-front" aria-label="Card front">
  <div class="front-brand">
    <span class="mark-square"></span>
    <span class="brand-name">KOVA WIRING</span>
  </div>

  <div class="person">
    <p class="person-name">Deren Whitcombe</p>
    <p class="person-role">Manager</p>
  </div>

  <address class="address" style="font-style:normal">
    57 Tannery Lane<br>
    #03-22 Silverbrook Industrial Complex<br>
    Singapore 347912
  </address>

  <ul class="contacts">
    <li>
      <svg viewBox="0 0 12 12"><path d="M2 1h3l1 3-2 1a6 6 0 0 0 3 3l1-2 3 1v3c-6 0-10-4-10-10z" fill="var(--green)"/></svg>
      (65) 61230458
    </li>
    <li>
      <svg viewBox="0 0 12 12"><rect x="3" y="0.5" width="6" height="11" rx="1" fill="var(--green)"/><rect x="4" y="2" width="4" height="7" fill="#fff"/></svg>
      (65) 90417726
    </li>
    <li>
      <svg viewBox="0 0 12 12"><rect x="1" y="4" width="10" height="6" fill="var(--green)"/><rect x="3" y="1" width="6" height="4" fill="none" stroke="var(--green)"/></svg>
      (65) 61230459
    </li>
    <li>
      <svg viewBox="0 0 12 12"><rect x="0.5" y="2" width="11" height="8" fill="var(--green)"/><path d="M1 2.5l5 4 5-4" fill="none" stroke="#fff"/></svg>
      derenkovawiring@mailbox-example.net
    </li>
  </ul>

  <svg class="bands" viewBox="0 0 700 140" preserveAspectRatio="none" aria-hidden="true">
    <polygon points="0,118 700,54 700,70 0,126" fill="var(--green)"/>
    <polygon points="0,126 700,70 700,88 0,134" fill="var(--blue)"/>
    <polygon points="0,134 700,88 700,140 0,140" fill="var(--navy)"/>
  </svg>
</section>

</body>
</html>
```